Real Estate For Sale Signage

I'm an independent agent in Lismore NSW Australia with high standards and looking for a catching 'For Sale'sign board.
I like classy, elegant, stylish and simple best.
My colours are red, white and black.
I don't have a logo or other font designs I need to stick to. I like the concept of a house or real estate design.
Before I created this project I played around on publisher and created the PDF attached. I'm not sold on it, but I don't mind the way the name has been layed out. Originally I had a white background with black & red font.
Fancy fonts for my name would be nice, but must not be busy.
Updates

Just wanted to advise that I have updated my brief and used the tools available to help get my ideas through.

Thank you for your work and time.

Kind regards
Marella

Industry/Entity Type

Real Estate

Requirements
Must have
• For Sale
Marella Quint Real Estate (must stand out)
0400 517 382 (must stand out)
17 Tallowood Street North Lismore
www.marellaquintrealestate.com.au

```html
<!DOCTYPE html>
<html lang="en">
<head>
<meta charset="utf-8">
<title>Marella Quint Real Estate – For Sale</title>
<link rel="stylesheet" href="https://fonts.googleapis.com/css2?family=Jost:wght@400;500&display=swap">
<style>
  :root {
    --brand-red: #e31b3b;
    --panel-charcoal: #3a3a3c;
    --text-white: #ffffff;
    --page-bg: #ffffff;
  }
  * { box-sizing: border-box; margin: 0; padding: 0; }
  html, body {
    width: 849px;
    height: 1200px;
    overflow: hidden;
    background: var(--page-bg);
  }
  .sign {
    position: relative;
    width: 849px;
    height: 1200px;
    overflow: hidden;
    font-family: "Jost", "Futura", sans-serif;
    color: var(--text-white);
  }
  .sign__background {
    position: absolute;
    inset: 0;
    background: var(--brand-red);
  }
  .sign__panel {
    position: absolute;
    left: 0;
    top: 0;
    width: 849px;
    height: 1200px;
  }
  .sign__panel path { fill: var(--panel-charcoal); }

  .brand {
    position: absolute;
    right: 49px;
    top: 82px;
    text-align: right;
  }
  .brand__name {
    font-size: 54px;
    font-weight: 400;
    line-height: 1;
    letter-spacing: 1px;
  }
  .brand__tagline {
    margin-top: 14px;
    font-size: 24px;
    font-weight: 400;
    letter-spacing: 2px;
  }

  .address {
    position: absolute;
    right: 49px;
    top: 238px;
    text-align: right;
    font-style: normal;
    font-size: 33px;
    line-height: 41px;
    letter-spacing: 2.5px;
  }

  .for-sale {
    position: absolute;
    left: 148px;
    top: 732px;
    transform: translate(-50%, -50%) rotate(-90deg);
    white-space: nowrap;
    font-size: 80px;
    font-weight: 500;
    letter-spacing: 16px;
    line-height: 1;
  }

  .phones {
    position: absolute;
    right: 30px;
    top: 882px;
    text-align: right;
    font-size: 68px;
    line-height: 74px;
    letter-spacing: 4px;
  }

  .website {
    position: absolute;
    right: 32px;
    top: 1106px;
    font-size: 31px;
    letter-spacing: 1.5px;
  }
</style>
</head>
<body>
  <main class="sign">
    <div class="sign__background" role="img" aria-label="Red background with a faint repeating pattern of house icons"></div>

    <svg class="sign__panel" viewBox="0 0 849 1200" aria-hidden="true">
      <path d="M0 0 H320 Q365 0 365 48 V236 Q365 278 330 290 Q294 302 294 340 V1200 H0 Z"/>
    </svg>

    <header class="brand">
      <h1 class="brand__name">Marella Quint</h1>
      <p class="brand__tagline">REAL ESTATE</p>
    </header>

    <address class="address">
      17 TALLOWOOD ST<br>
      NORTH LISMORE<br>
      NSW
    </address>

    <p class="for-sale">FOR SALE WITH</p>

    <p class="phones">
      <span class="phones__mobile">0400 517 382</span><br>
      <span class="phones__office">02 6600 4915</span>
    </p>

    <p class="website">marellaquintrealestate.com.au</p>
  </main>
</body>
</html>
```